Redesign Employer Form

We need to consolidate the form located at: Tellawindor.com to be one form instead of the multiple screens that currently exist. The new form must be user friendly with a layout that supports the collection of the various pieces of information currently displayed on the site.

```html
<!DOCTYPE html>
<html lang="en">
<head>
<meta charset="utf-8">
<title>Tellawindor – Pay Stub Form</title>
<link rel="stylesheet" href="https://fonts.googleapis.com/css2?family=Open+Sans:wght@400;600;700&display=swap">
<style>
:root{
  --blue:#1f56c9;
  --blue-dark:#0b3aa0;
  --blue-title:#1446a8;
  --panel-bg:#ebebeb;
  --panel-border:#cfcfcf;
  --dark-head-top:#4a4a4a;
  --dark-head-bottom:#2c2c2c;
  --text:#333;
  --muted:#555;
  --input-border:#c9c9c9;
  --red:#d62323;
  --footer:#262626;
  --footer-text:#e6e6e6;
  --green:#5cc626;
}
*{box-sizing:border-box;margin:0;padding:0}
html,body{width:1200px;height:2853px;overflow:hidden}
body{position:relative;background:#fff;font-family:"Open Sans",Arial,sans-serif;color:var(--text)}

.site-header{position:absolute;left:0;top:0;width:1200px;height:95px;background:linear-gradient(180deg,#2a63d6,#0f3ea8)}
.site-header .region-art{position:absolute;right:0;top:0;width:344px;height:95px;background:linear-gradient(90deg,rgba(30,80,190,0),#3c7a6a 60%,#2f5fb0)}
.brand{position:absolute;left:99px;top:12px;display:flex;align-items:center;gap:12px}
.brand-dot{width:72px;height:72px;border-radius:50%;background:#fff}
.brand-name{color:#fff;font-weight:700;font-size:30px}
.delivery-badge{position:absolute;left:730px;top:-8px;width:116px;height:108px;border-radius:50%;background:var(--green);display:flex;flex-direction:column;align-items:center;justify-content:center;color:#fff;font-weight:700;line-height:1.05}
.delivery-badge .top{font-size:18px;color:#123}
.delivery-badge .price{font-size:22px;margin-top:4px}

.page-title{position:absolute;top:148px;left:0;width:1200px;text-align:center;color:var(--blue-title);font-size:26px;font-weight:700}

.panel{position:absolute;left:101px;width:1000px;background:var(--panel-bg);border:1px solid var(--panel-border);border-radius:4px;overflow:hidden}
.panel-head{height:63px;display:flex;align-items:center;justify-content:space-between;padding:0 18px 0 16px;color:#fff;font-size:23px;background:linear-gradient(180deg,var(--dark-head-top),var(--dark-head-bottom))}
.panel-head.primary{background:linear-gradient(180deg,#3a73e0,#1a4cc0)}
.step{display:flex;align-items:center;gap:10px;font-size:23px}
.step-num{width:34px;height:34px;border-radius:50%;background:#f2f2f2;color:#333;font-size:20px;display:flex;align-items:center;justify-content:center}
.panel-body{padding:26px 17px 25px}

.grid{display:grid;grid-template-columns:314px 314px 314px;column-gap:11px;row-gap:27px}
.field label{display:block;font-size:14px;line-height:18px;margin-bottom:6px;color:var(--text)}
.input{height:42px;background:#fff;border:1px solid var(--input-border);border-radius:4px;font-size:14px;color:#555;display:flex;align-items:center;padding:0 12px;justify-content:space-between}
.input.select{color:#666}
.caret{width:0;height:0;border-left:6px solid transparent;border-right:6px solid transparent;border-top:8px solid #333}
.placeholder{color:#888}

.abs{position:absolute}
.lbl{font-size:14px;color:var(--text)}
.salary{left:17px;width:314px;display:flex}
.salary .cur{width:42px;height:42px;background:var(--blue);color:#fff;display:flex;align-items:center;justify-content:center;border-radius:4px 0 0 4px;font-size:16px}
.salary .input{flex:1;border-radius:0 4px 4px 0;border-left:none}
.radio{display:flex;align-items:center;gap:10px;font-size:14px;color:var(--muted)}
.radio i{width:15px;height:15px;border-radius:50%;border:1px solid #aaa;background:#f8f8f8}
.check i{border-radius:3px}

.btn{position:absolute;height:46px;border-radius:5px;color:#fff;font-size:15px;display:flex;align-items:center;justify-content:center;text-transform:uppercase;box-shadow:0 1px 3px rgba(0,0,0,.3)}
.btn-blue{background:linear-gradient(180deg,#4a82ec,#1a4cc0)}
.btn-red{background:linear-gradient(180deg,#ee4a3e,#c41b14)}
.btn-dark{background:linear-gradient(180deg,#666,#333)}
.small-text{font-size:14px;line-height:24px;color:var(--text)}
.section-link{font-size:16px;color:var(--blue-title)}

.site-footer{position:absolute;left:0;top:2501px;width:1200px;height:291px;background:var(--footer);color:var(--footer-text)}
.badge-shape{position:absolute;background:#ddd;border-radius:8px}
.foot-head{position:absolute;top:76px;font-size:17px;font-weight:600;color:#fff}
.foot-list{position:absolute;top:112px;list-style:none;font-size:14px;line-height:32px}
.contact-row{position:absolute;display:flex;gap:14px;font-size:14px;line-height:20px;color:#fff}
.contact-row svg{flex:none}
.foot-input{position:absolute;left:873px;width:224px;height:35px;border:1px solid #888;background:#1e1e1e;font-size:13px;color:#ddd;padding:0 10px;display:flex;align-items:center}
.foot-btn{position:absolute;left:873px;top:205px;width:224px;height:33px;background:var(--blue);color:#fff;font-size:13px;display:flex;align-items:center;justify-content:center}
.bottom-bar{position:absolute;left:0;top:2792px;width:1200px;height:61px;background:linear-gradient(180deg,#2a63d6,#1446b8);color:#fff;font-size:14px}
.bottom-bar .copy{position:absolute;left:101px;top:20px}
.social{position:absolute;top:15px;width:30px;height:30px;border-radius:50%;border:2px solid #fff}
</style>
</head>
<body>

<header class="site-header">
  <div class="region-art" role="img" aria-label="Faint state map decoration"></div>
  <div class="brand"><span class="brand-dot"></span><span class="brand-name">Tellawindor.com</span></div>
  <div class="delivery-badge"><span class="top">Instant<br>Delivery</span><span class="price">$7.95</span></div>
</header>

<h1 class="page-title">The ORIGINAL Sample Pay Stub for Virginia Employees</h1>

<!-- Step 1 -->
<section class="panel" style="top:236px;height:276px">
  <div class="panel-head primary"><span>Company Information:</span><span class="step">Step: <span class="step-num">1</span></span></div>
  <div class="panel-body">
    <div class="grid">
      <div class="field"><label>Company Name*</label><div class="input"></div></div>
      <div class="field"><label>Company Address (optional)</label><div class="input"></div></div>
      <div class="field"><label>Company Zip Code (optional)</label><div class="input"></div></div>
      <div class="field"><label>Company Phone Number (optional)</label><div class="input"></div></div>
      <div class="field"><label>Company EIN / SSN (optional)</label><div class="input"></div></div>
    </div>
  </div>
</section>

<!-- Step 2 -->
<section class="panel" style="top:544px;height:375px">
  <div class="panel-head"><span>Employee Information:</span><span class="step">Step: <span class="step-num">2</span></span></div>
  <div class="panel-body">
    <div class="grid">
      <div class="field"><label>Employee Name*</label><div class="input"></div></div>
      <div class="field"><label>Employee SSN (Last 4 digits)*</label><div class="input"></div></div>
      <div class="field"><label>Employee Address (optional)</label><div class="input"></div></div>
      <div class="field"><label>Employee Zip Code (optional)</label><div class="input"></div></div>
      <div class="field"><label>Employee ID (optional)</label><div class="input"></div></div>
      <div class="field"><label>Marital Status</label><div class="input select">Single<span class="caret"></span></div></div>
      <div class="field"><label>Number Of Dependants</label><div class="input select">0<span class="caret"></span></div></div>
      <div class="field"><label>Age 65 And Over / Blind Exemptions</label><div class="input select">0<span class="caret"></span></div></div>
    </div>
  </div>
</section>

<!-- Step 3 -->
<section class="panel" style="top:951px;height:479px">
  <div class="panel-head"><span>Salary Information:</span><span class="step">Step: <span class="step-num">3</span></span></div>
  <span class="abs lbl" style="left:17px;top:86px">Annual Salary*</span>
  <div class="abs salary" style="top:116px"><span class="cur">$</span><div class="input">2522.00</div></div>
  <span class="abs lbl" style="left:17px;top:177px">Pay Frequency (Pay Period)*</span>
  <span class="abs radio" style="left:17px;top:221px"><i></i>Daily</span>
  <span class="abs radio" style="left:144px;top:221px"><i></i>Weekly (Ex: Every Friday)</span>
  <span class="abs radio" style="left:418px;top:221px"><i></i>Bi-Weekly (Ex: Every other Wed.)</span>
  <span class="abs radio" style="left:719px;top:221px"><i></i>Semi-Monthly (Ex: 1st and 16th)</span>
  <span class="abs radio" style="left:17px;top:272px"><i></i>Quarterly</span>
  <span class="abs radio" style="left:144px;top:272px"><i></i>Monthly (Ex: 1st of month only)</span>
  <span class="abs radio" style="left:418px;top:272px"><i></i>Semi-Annually</span>
  <span class="abs radio" style="left:719px;top:272px"><i></i>Annually</span>
  <span class="abs lbl" style="left:17px;top:316px">Choose First Pay Date(s) Needed*</span>
  <div class="abs input" style="left:17px;top:347px;width:314px">14 May 2016</div>
  <div class="btn btn-blue" style="left:350px;top:345px;width:190px">Add Next Paydate</div>
  <span class="abs radio check" style="left:17px;top:430px"><i></i>This employee was hired in 2016</span>
  <span class="abs radio check" style="left:306px;top:430px"><i></i>Show hourly rate on the stub</span>
</section>

<!-- Step 4 -->
<section class="panel" style="top:1465px;height:703px">
  <div class="panel-head"><span>Additional Income and Deductions:</span><span class="step">Step: <span class="step-num">4</span></span></div>
  <p class="abs small-text" style="left:17px;top:86px;width:966px">In addition to your pay and standard withholdings, add additional income and / or deductions. Additions and Deductions will be applied to each pay date requested below.</p>
  <span class="abs lbl" style="left:17px;top:166px">Additions (Description / Current Amount / YTD Amount)</span>
  <div class="abs input" style="left:17px;top:197px;width:443px"><span class="placeholder">Ex: Tax Credit</span></div>
  <div class="abs input" style="left:472px;top:197px;width:150px"><span class="placeholder">Ex: 100$</span></div>
  <div class="abs input" style="left:635px;top:197px;width:150px"><span class="placeholder">Ex: 500$</span></div>
  <div class="btn btn-red" style="left:797px;top:195px;width:100px">Delete</div>
  <div class="btn btn-blue" style="left:17px;top:256px;width:137px">Add Income</div>
  <span class="abs lbl" style="left:17px;top:325px">Deductions (Description / Current Amount / YTD Amount)</span>
  <div class="abs input" style="left:17px;top:356px;width:443px"><span class="placeholder">Ex: Tax Credit</span></div>
  <div class="abs input" style="left:472px;top:356px;width:150px"><span class="placeholder">Ex: 100$</span></div>
  <div class="abs input" style="left:635px;top:356px;width:150px"><span class="placeholder">Ex: 500$</span></div>
  <div class="btn btn-red" style="left:797px;top:354px;width:100px">Delete</div>
  <div class="btn btn-blue" style="left:17px;top:415px;width:137px">Add Deduction</div>
  <span class="abs section-link" style="left:17px;top:500px">Check Numbers:</span>
  <p class="abs small-text" style="left:17px;top:530px;width:966px">For your convenience, we have auto generated check numbers for each pay date you selected. Keep, modify, or delete the check numbers from your stubs.</p>
  <span class="abs lbl" style="left:17px;top:605px">Date:</span>
  <span class="abs lbl" style="left:506px;top:605px">Check #</span>
  <div class="abs input" style="left:17px;top:635px;width:477px">14 May 2016</div>
  <div class="abs input" style="left:506px;top:635px;width:475px">5643</div>
</section>

<!-- Step 5 -->
<section class="panel" style="top:2203px;height:241px">
  <div class="panel-head"><span>Finilization:</span><span class="step">Step: <span class="step-num">5</span></span></div>
  <p class="abs small-text" style="left:0;top:96px;width:1000px;text-align:center">Note: All watermarks and background images will be removed from your final document(s).</p>
  <div class="btn btn-blue" style="left:272px;top:157px;width:205px">Submit and Preview</div>
  <div class="btn btn-dark" style="left:504px;top:157px;width:222px">Download Your Stub</div>
</section>

<footer class="site-footer">
  <div class="badge-shape" style="left:118px;top:70px;width:181px;height:77px"></div>
  <div class="badge-shape" style="left:139px;top:185px;width:148px;height:57px"></div>

  <h3 class="foot-head" style="left:420px">QUICK LINKS</h3>
  <ul class="foot-list" style="left:420px">
    <li>&gt; Home</li><li>&gt; About Us</li><li>&gt; Features</li><li>&gt; FAQ</li><li>&gt; Contact Us</li>
  </ul>

  <h3 class="foot-head" style="left:609px">CONTACT US</h3>
  <div class="contact-row" style="left:604px;top:115px">
    <svg width="26" height="26" viewBox="0 0 26 26"><circle cx="13" cy="13" r="11" fill="none" stroke="#fff" stroke-width="2"/><path d="M13 6a4.5 4.5 0 0 0-4.5 4.5c0 3.5 4.5 8.5 4.5 8.5s4.5-5 4.5-8.5A4.5 4.5 0 0 0 13 6z" fill="#fff"/></svg>
    <span>Address:<br>Harlow Rd, Unit 42 -<br>Eastmoor</span>
  </div>
  <div class="contact-row" style="left:604px;top:198px">
    <svg width="26" height="26" viewBox="0 0 26 26"><circle cx="13" cy="13" r="11" fill="none" stroke="#fff" stroke-width="2"/><rect x="7" y="9" width="12" height="8" fill="none" stroke="#fff" stroke-width="1.5"/><path d="M7 9l6 5 6-5" fill="none" stroke="#fff" stroke-width="1.5"/></svg>
    <span style="line-height:26px">Email: Tellawindor.com</span>
  </div>
  <div class="contact-row" style="left:604px;top:240px">
    <svg width="26" height="26" viewBox="0 0 26 26"><circle cx="13" cy="13" r="11" fill="none" stroke="#fff" stroke-width="2"/><path d="M9 8l2.5-.5 1.5 3-1.5 1.2a7 7 0 0 0 3 3l1.2-1.5 3 1.5L18 17c-5 .5-9.5-4-9-9z" fill="#fff"/></svg>
    <span style="line-height:26px">Phone: +1800 0000 0142</span>
  </div>

  <h3 class="foot-head" style="left:873px">CONTACT FORM</h3>
  <div class="foot-input" style="top:110px">Name</div>
  <div class="foot-input" style="top:158px">Email</div>
  <div class="foot-btn">SIGN UP NOW</div>
</footer>

<div class="bottom-bar">
  <span class="copy">© 2016 Tellawindor. All Rights Reserved</span>
  <span class="social" style="left:932px"></span>
  <span class="social" style="left:978px"></span>
  <span class="social" style="left:1023px"></span>
  <span class="social" style="left:1069px"></span>
</div>

</body>
</html>
```